Velura Skincare packaging designs

We are need to create packaging for our skincare brand. We need two designs. One for round jars which is for creams/capsules and the second will be for bottles/serums Some products will be larger in size so please ensure the packaging design will work and there isn't a lot white/empty space

Below are the names of some of our products.
Screw-On Top Jar (25 pads- 4 inches wide) - Brisk Wipes I Glow Lifting Rounds
Pump Bottle (2 oz) - AquaMEND I Hyaluronic Acid + Vitamin Serum
Pump Bottle (6oz) - The Oat Rinse I Conditioning Face Cleanser
Dropper bottle (1 oz) - Morning Mist I Hydrating Moisturizer
Cream jar (1.5 oz) - Morning Mist I Hydrating Moisturizer
Capsules Jar (25 capsules in a jar)- Plume Drop I Moisture + Hydrating Capsules
Capsules Jar (25 capsules in a jar) - Clear Pulse I Impurity Capsules

We will also need help with the packing design in terms of layout of the logo, item name, desc, and ingredients on each product.

Target Market(s)

women

Industry/Entity Type

skincare, beauty

Font styles to use
Sans Serif

Colors
E54698
E96AAD
F1A4CE
F9D9EA
FCEFF6

Requirements
Must have
• Pantone color is 2052 CP HEX #DAAFCA (218 , 175 , 202)

```html
<!DOCTYPE html>
<html lang="en">
<head>
<meta charset="utf-8">
<title>The Oat Rinse – Cleansing Lotion Label</title>
<link rel="stylesheet" href="https://fonts.googleapis.com/css2?family=Quicksand:wght@400;500;600&display=swap">
<style>
  :root {
    --page-bg: #ffffff;
    --pink-deep: #f59bba;
    --pink-mid: #f6b3c9;
    --pink-light: #f8c6d6;
    --ink: #3a3a3a;
    --ink-soft: #9a9a9a;
    --band-white: #ffffff;
    --band-grey: #b9b9b9;
    --brand-ink: #ffffff;
  }
  * { margin: 0; padding: 0; box-sizing: border-box; }
  html, body {
    width: 1200px;
    height: 1000px;
    overflow: hidden;
    background: var(--page-bg);
    font-family: "Quicksand", sans-serif;
  }
  .label {
    position: absolute;
    left: 290px;
    top: 60px;
    width: 621px;
    height: 880px;
    background: linear-gradient(90deg,
      var(--pink-deep) 0%,
      var(--pink-light) 20%,
      var(--pink-mid) 42%,
      var(--pink-light) 56%,
      var(--pink-deep) 70%,
      var(--pink-light) 90%,
      var(--pink-mid) 100%);
  }
  .brand {
    position: absolute;
    left: 0;
    top: 160px;
    width: 100%;
    display: flex;
    align-items: center;
    justify-content: center;
    gap: 14px;
  }
  .brand-dot {
    width: 18px;
    height: 18px;
    border-radius: 50%;
    background: var(--brand-ink);
  }
  .brand-name {
    color: var(--brand-ink);
    font-weight: 500;
    font-size: 34px;
    letter-spacing: 1px;
    line-height: 1;
  }
  .name-band {
    position: absolute;
    left: 52px;
    top: 371px;
    width: 517px;
    height: 84px;
    background: linear-gradient(90deg,
      var(--band-white) 0%,
      var(--band-grey) 30%,
      var(--band-white) 52%,
      var(--band-grey) 80%,
      var(--band-white) 100%);
    display: flex;
    align-items: center;
    justify-content: center;
  }
  .product-name {
    color: var(--ink);
    font-weight: 500;
    font-size: 52px;
    letter-spacing: 0.5px;
    white-space: nowrap;
  }
  .type-band {
    position: absolute;
    left: 52px;
    top: 455px;
    width: 517px;
    height: 64px;
    background: var(--band-white);
    display: flex;
    align-items: center;
    justify-content: center;
  }
  .product-type {
    color: var(--ink-soft);
    font-weight: 500;
    font-size: 29px;
    letter-spacing: 0.5px;
  }
  .volume {
    position: absolute;
    left: 0;
    top: 796px;
    width: 100%;
    text-align: center;
    color: var(--ink);
    font-weight: 500;
    font-size: 29px;
    letter-spacing: 0.5px;
  }
</style>
</head>
<body>
  <main class="label">
    <div class="brand">
      <span class="brand-dot"></span>
      <span class="brand-name">Petalin</span>
    </div>
    <div class="name-band">
      <h1 class="product-name">The Oat Rinse</h1>
    </div>
    <div class="type-band">
      <p class="product-type">Cleansing Lotion</p>
    </div>
    <p class="volume">6 fl. oz (177ml)</p>
  </main>
</body>
</html>
```